Pay-Per-Use Production Space Warehouse/Factory/Production Space

Please refer to project requirements as attached/included. This is an introductory marketing Info graphic to capture attention or create awareness to a new, epic and unique business value preposition and business model for customer to easily launch new products/services and robust supply chain. This is a win win revolutionary business solution compare with traditional or conventional methods of outsourcing or DIY design, build, finance, operate and maintain. PROJECT Requirement to info graphic designer
1) Subject to confidentiality and all rights reserved
2) Below are some photos which you may consider to use for this work
3) Clarify and verify with us if there are any questions related to this work and design

Target Market(s)

Global, (Life sciences, food, others)

Industry/Entity Type

Medical And Science

Requirements
Must have
• Dynamic background template.
Should not have
• Monotonous and un-creative designs

```html
<!DOCTYPE html>
<html lang="en">
<head>
<meta charset="utf-8">
<title>Pay-Per-Use Production Space – Info Flyer</title>
<link href="https://fonts.googleapis.com/css2?family=Questrial&display=swap" rel="stylesheet">
<style>
  :root {
    --canvas-bg: #d9cbf9;
    --deep-violet: #5a20b8;
    --magenta: #b43a9f;
    --hot-pink: #f2527c;
    --sky: #7cc3ea;
    --orange: #f7a531;
    --lime: #8cc63f;
    --coral: #ef5f5a;
    --violet: #7b1ff2;
    --cyan: #07e3f5;
    --royal: #2f3cf0;
    --pine: #3f6b5a;
    --white: #ffffff;
    --bulb: #fbb315;
  }
  html, body {
    margin: 0;
    padding: 0;
    width: 1200px;
    height: 749px;
    overflow: hidden;
    background: var(--canvas-bg);
  }
  .canvas {
    position: relative;
    width: 1200px;
    height: 749px;
  }
  .flyer {
    position: absolute;
    top: 90px;
    width: 432px;
    height: 561px;
  }
  .flyer--front { left: 121px; }
  .flyer--back { left: 651px; }
  .flyer svg { display: block; }
  .copy {
    font-family: "Questrial", "Century Gothic", sans-serif;
    fill: var(--white);
    text-anchor: middle;
  }
  .copy--sm { font-size: 10px; }
  .copy--md { font-size: 11.5px; }
  .copy--note { font-size: 10px; }
  .copy--head { font-size: 12px; text-anchor: start; }
  .timeline { stroke: var(--white); stroke-width: 5; stroke-linecap: round; }
  .node { fill: var(--white); }
  .callout { fill: none; stroke-width: 2.5; stroke-linejoin: round; }
  .badge-core { fill: var(--white); }
</style>
</head>
<body>
<div class="canvas">

  <!-- Front flyer -->
  <section class="flyer flyer--front">
    <svg width="432" height="561" viewBox="0 0 432 561">
      <defs>
        <linearGradient id="front-bg" x1="0" y1="0" x2="0.4" y2="1">
          <stop offset="0" stop-color="#5a20b8"/>
          <stop offset="0.55" stop-color="#c2409a"/>
          <stop offset="1" stop-color="#a83aa6"/>
        </linearGradient>
        <radialGradient id="front-glow" cx="0.6" cy="0.55" r="0.5">
          <stop offset="0" stop-color="#f6577a" stop-opacity="0.9"/>
          <stop offset="1" stop-color="#f6577a" stop-opacity="0"/>
        </radialGradient>
        <linearGradient id="front-wave" x1="0" y1="0" x2="0" y2="1">
          <stop offset="0" stop-color="#07e6f6"/>
          <stop offset="1" stop-color="#3a2ef0"/>
        </linearGradient>
      </defs>

      <rect class="flyer-bg" width="432" height="561" fill="url(#front-bg)"/>
      <rect class="flyer-glow" width="432" height="561" fill="url(#front-glow)"/>

      <!-- bottom waves -->
      <path d="M0 520 C70 475 150 462 230 478 C300 492 360 520 432 492 L432 561 L0 561Z" fill="#5a4bee"/>
      <path d="M0 530 C90 495 170 500 250 515 C330 530 390 528 432 510 L432 561 L0 561Z" fill="url(#front-wave)"/>
      <text class="copy copy--note" x="216" y="547">*Other technical, financial, project and operational solutions are also available</text>

      <line class="timeline" x1="221" y1="29" x2="221" y2="458"/>
      <circle class="node" cx="221" cy="57" r="10"/>
      <circle class="node" cx="221" cy="148" r="10"/>
      <circle class="node" cx="221" cy="241" r="10"/>
      <circle class="node" cx="221" cy="334" r="10"/>
      <circle class="node" cx="221" cy="426" r="10"/>

      <!-- Step 1: idea -->
      <g class="badge badge--idea">
        <path d="M150 47 H182 V36 L198 57 L182 78 V67 H150Z" fill="var(--sky)"/>
        <circle cx="124" cy="57" r="45" fill="var(--sky)"/>
        <circle class="badge-core" cx="124" cy="57" r="32"/>
        <circle cx="124" cy="51" r="13" fill="var(--bulb)"/>
        <rect x="118" y="62" width="12" height="10" fill="var(--bulb)"/>
        <rect x="117" y="72" width="14" height="3" rx="1.5" fill="#555"/>
        <rect x="118" y="76" width="12" height="3" rx="1.5" fill="#555"/>
        <g stroke="var(--bulb)" stroke-width="2" stroke-linecap="round">
          <line x1="124" y1="31" x2="124" y2="34"/>
          <line x1="106" y1="51" x2="103" y2="51"/>
          <line x1="142" y1="51" x2="145" y2="51"/>
          <line x1="111" y1="38" x2="109" y2="36"/>
          <line x1="137" y1="38" x2="139" y2="36"/>
        </g>
      </g>
      <path class="callout" d="M266 21 H376 Q386 21 386 31 V88 Q386 98 376 98 H266 Q256 98 256 88 V66 L240 57 L256 48 V31 Q256 21 266 21Z" stroke="var(--sky)"/>
      <text class="copy copy--sm">
        <tspan x="321" y="33">Through Our Patented &amp;</tspan>
        <tspan x="321" y="45">Innovative Factory Space</tspan>
        <tspan x="321" y="57">Design, Unique Business</tspan>
        <tspan x="321" y="69">Model, Due Diligence and</tspan>
        <tspan x="321" y="81">Mutual Adoption of Good</tspan>
        <tspan x="321" y="93">Practises</tspan>
      </text>

      <!-- Step 2: pay-per-use -->
      <path class="callout" d="M65 118 H171 Q181 118 181 128 V139 L198 148 L181 157 V176 Q181 186 171 186 H65 Q55 186 55 176 V128 Q55 118 65 118Z" stroke="var(--orange)"/>
      <text class="copy copy--md">
        <tspan x="118" y="132">PAY-PER-USE</tspan>
        <tspan x="118" y="152">Factory/Warehouse/</tspan>
        <tspan x="118" y="172">Production Space*</tspan>
      </text>
      <g class="badge badge--gears">
        <path d="M292 138 H260 V127 L244 148 L260 169 V158 H292Z" fill="var(--orange)"/>
        <circle cx="317" cy="148" r="45" fill="var(--orange)"/>
        <circle class="badge-core" cx="317" cy="148" r="32"/>
        <circle cx="307" cy="143" r="9" fill="none" stroke="#ee4a23" stroke-width="7" stroke-dasharray="3.5 3"/>
        <circle cx="307" cy="143" r="6" fill="none" stroke="#ee4a23" stroke-width="5"/>
        <circle cx="331" cy="146" r="5" fill="none" stroke="var(--orange)" stroke-width="5" stroke-dasharray="2.5 2"/>
        <circle cx="331" cy="146" r="3.5" fill="none" stroke="var(--orange)" stroke-width="3"/>
        <circle cx="322" cy="162" r="3.5" fill="none" stroke="#9b4bc4" stroke-width="4" stroke-dasharray="2 1.6"/>
      </g>

      <!-- Step 3: audience -->
      <g class="badge badge--client">
        <path d="M150 231 H182 V220 L198 241 L182 262 V251 H150Z" fill="var(--lime)"/>
        <circle cx="124" cy="241" r="45" fill="var(--lime)"/>
        <circle class="badge-core" cx="124" cy="241" r="32"/>
        <circle cx="124" cy="241" r="26" fill="var(--pine)" opacity="0.85" role="img" aria-label="Icon of a business client in a suit"/>
      </g>
      <path class="callout" d="M268 211 H373 Q383 211 383 221 V269 Q383 279 373 279 H268 Q258 279 258 269 V250 L242 241 L258 232 V221 Q258 211 268 211Z" stroke="var(--lime)"/>
      <text class="copy copy--sm">
        <tspan x="321" y="224">Pay-Per-Use Applicable</tspan>
        <tspan x="321" y="235.5">to All Start Ups/</tspan>
        <tspan x="321" y="247">Small Medium Enterprises/</tspan>
        <tspan x="321" y="258.5">Multinational</tspan>
        <tspan x="321" y="270">Corporations/Others</tspan>
      </text>

      <!-- Step 4: growth -->
      <path class="callout" d="M72 303 H176 Q186 303 186 313 V325 L201 334 L186 343 V371 Q186 381 176 381 H72 Q62 381 62 371 V313 Q62 303 72 303Z" stroke="var(--coral)"/>
      <text class="copy copy--sm">
        <tspan x="124" y="313">Through Our Patented &amp;</tspan>
        <tspan x="124" y="324.5">Innovative Factory Space</tspan>
        <tspan x="124" y="336">Design, Unique Business</tspan>
        <tspan x="124" y="347.5">Model, Due Diligence</tspan>
        <tspan x="124" y="359">and Mutual Adoption of</tspan>
        <tspan x="124" y="370.5">Good Practises</tspan>
      </text>
      <g class="badge badge--growth">
        <path d="M292 324 H260 V313 L244 334 L260 355 V344 H292Z" fill="var(--coral)"/>
        <circle cx="317" cy="334" r="45" fill="var(--coral)"/>
        <circle class="badge-core" cx="317" cy="334" r="32"/>
        <rect x="302" y="336" width="7" height="13" fill="#29a9e1"/>
        <rect x="311" y="327" width="7" height="22" fill="#3dbf8f"/>
        <rect x="320" y="318" width="7" height="31" fill="var(--pine)"/>
        <line x1="300" y1="351" x2="329" y2="351" stroke="#29a9e1" stroke-width="1.5"/>
        <path d="M303 329 L317 317" stroke="var(--orange)" stroke-width="2.5" stroke-linecap="round"/>
        <path d="M313 315 L320 314 L319 321Z" fill="var(--orange)"/>
      </g>

      <!-- Step 5: global -->
      <g class="badge badge--globe">
        <path d="M150 416 H182 V405 L198 426 L182 447 V436 H150Z" fill="var(--violet)"/>
        <circle cx="124" cy="426" r="45" fill="var(--violet)"/>
        <circle class="badge-core" cx="124" cy="426" r="32"/>
        <circle cx="124" cy="426" r="24" fill="#2a8fd8"/>
        <g fill="none" stroke="var(--white)" stroke-width="2">
          <ellipse cx="124" cy="426" rx="10" ry="24"/>
          <line x1="124" y1="402" x2="124" y2="450"/>
          <line x1="100" y1="426" x2="148" y2="426"/>
          <path d="M104 414 H144 M104 438 H144"/>
        </g>
      </g>
      <path class="callout" d="M268 396 H373 Q383 396 383 406 V454 Q383 464 373 464 H268 Q258 464 258 454 V435 L242 426 L258 417 V406 Q258 396 268 396Z" stroke="var(--violet)"/>
      <text class="copy copy--sm">
        <tspan x="321" y="409">Anywhere in the World as</tspan>
        <tspan x="321" y="420.5">Mutually Agreed</tspan>
        <tspan x="321" y="432">(Immediate Sites Available</tspan>
        <tspan x="321" y="443.5">in Singapore and</tspan>
        <tspan x="321" y="455">Indonesia)</tspan>
      </text>
    </svg>
  </section>

  <!-- Back flyer -->
  <section class="flyer flyer--back">
    <svg width="432" height="561" viewBox="0 0 432 561">
      <defs>
        <linearGradient id="back-bg" x1="0" y1="0" x2="0.4" y2="1">
          <stop offset="0" stop-color="#5a20b8"/>
          <stop offset="0.5" stop-color="#c2409a"/>
          <stop offset="1" stop-color="#e04f82"/>
        </linearGradient>
        <radialGradient id="back-glow" cx="0.55" cy="0.55" r="0.5">
          <stop offset="0" stop-color="#f6577a" stop-opacity="0.9"/>
          <stop offset="1" stop-color="#f6577a" stop-opacity="0"/>
        </radialGradient>
        <linearGradient id="back-header" x1="0" y1="0" x2="0" y2="1">
          <stop offset="0" stop-color="#08b8fb"/>
          <stop offset="1" stop-color="#2536f2"/>
        </linearGradient>
        <linearGradient id="back-wave" x1="0" y1="0" x2="1" y2="0">
          <stop offset="0" stop-color="#3b3cf2"/>
          <stop offset="0.6" stop-color="#9b56ea"/>
          <stop offset="1" stop-color="#c06ae8"/>
        </linearGradient>
        <linearGradient id="site-tone" x1="0" y1="0" x2="1" y2="1">
          <stop offset="0" stop-color="#5c5f4e"/>
          <stop offset="0.5" stop-color="#a9a59a"/>
          <stop offset="1" stop-color="#6b5a44"/>
        </linearGradient>
      </defs>

      <rect class="flyer-bg" width="432" height="561" fill="url(#back-bg)"/>
      <rect class="flyer-glow" width="432" height="561" fill="url(#back-glow)"/>

      <rect x="207" y="17" width="225" height="37" rx="8" fill="#3a2ff0"/>
      <rect x="210" y="20" width="222" height="32" rx="7" fill="url(#back-header)"/>
      <text class="copy copy--head" x="221" y="41">Lumina Design Requirements Intent</text>

      <line class="timeline" x1="215" y1="67" x2="215" y2="250"/>
      <circle class="node" cx="215" cy="103" r="10"/>
      <circle class="node" cx="215" cy="207" r="10"/>

      <!-- Pricing principle -->
      <g class="badge badge--pie">
        <path d="M136 93 H168 V82 L184 103 L168 124 V113 H136Z" fill="var(--lime)"/>
        <circle cx="110" cy="103" r="45" fill="var(--lime)"/>
        <circle class="badge-core" cx="110" cy="103" r="32"/>
        <path d="M110 103 L110 79 A24 24 0 1 0 132 112 Z" fill="var(--pine)"/>
        <path d="M114 99 L114 75 A24 24 0 0 1 136 108 Z" fill="none" stroke="var(--pine)" stroke-width="2"/>
        <g stroke="var(--pine)" stroke-width="1.2">
          <line x1="118" y1="98" x2="124" y2="80"/>
          <line x1="121" y1="100" x2="129" y2="84"/>
          <line x1="125" y1="102" x2="133" y2="90"/>
          <line x1="129" y1="104" x2="135" y2="97"/>
        </g>
      </g>
      <path class="callout" d="M270 71 H375 Q385 71 385 81 V129 Q385 139 375 139 H270 Q260 139 260 129 V112 L244 103 L260 94 V81 Q260 71 270 71Z" stroke="var(--lime)"/>
      <text class="copy copy--sm">
        <tspan x="323" y="83">You use it, you pay it**</tspan>
        <tspan x="323" y="94.7">You don’t use the</tspan>
        <tspan x="323" y="106.4">Production Space, You</tspan>
        <tspan x="323" y="118.1">Don’t pay for it!</tspan>
        <tspan x="323" y="129.8">Partial Use, Partial Pay</tspan>
      </text>

      <!-- Existing customers -->
      <path class="callout" d="M63 178 H168 Q178 178 178 188 V198 L196 207 L178 216 V235 Q178 245 168 245 H63 Q53 245 53 235 V188 Q53 178 63 178Z" stroke="var(--violet)"/>
      <text class="copy copy--md">
        <tspan x="116" y="193">Our Existing</tspan>
        <tspan x="116" y="213">Customers include</tspan>
        <tspan x="116" y="233">Food &amp; Life Science</tspan>
      </text>
      <g class="badge badge--customers">
        <path d="M300 197 H267 V186 L251 207 L267 228 V217 H300Z" fill="var(--violet)"/>
        <circle cx="325" cy="207" r="45" fill="var(--violet)"/>
        <circle class="badge-core" cx="325" cy="207" r="32"/>
        <circle cx="325" cy="207" r="26" fill="#2a8fd8" opacity="0.8" role="img" aria-label="Icon of two customers in conversation with speech bubbles"/>
      </g>

      <text class="copy copy--sm">
        <tspan x="216" y="267">Value Propositions**:</tspan>
        <tspan x="216" y="279">Maximum Technical and Financial Flexibility to Scale Up or Down with Ease. This will allow</tspan>
        <tspan x="216" y="290.5">you to Mitigate Risks, Change Swiftly and to Engage Success Better</tspan>
        <tspan x="216" y="302">If Apply &amp; Use Continuously, its Gives Your Organization New Strategic Option</tspan>
        <tspan x="216" y="313.5">to Gain the Competitive Advantage to Launch New Products/Services and or Robust Supply</tspan>
        <tspan x="216" y="325">Chain  “Cheaper”, Better, Faster &amp; Assured</tspan>
        <tspan x="216" y="354">Contact us at PayPerUse@lumina-spaces.example</tspan>
      </text>

      <!-- Facility visual -->
      <path d="M0 420 C70 372 150 365 230 388 C310 410 380 415 432 380 L432 561 L0 561Z" fill="url(#back-wave)"/>
      <path d="M0 470 C60 415 150 380 230 400 C310 420 390 430 432 410 L432 561 L0 561Z" fill="url(#site-tone)" role="img" aria-label="Aerial 3D cutaway render of a multi-room production facility with equipment and storage racks"/>
    </svg>
  </section>

</div>
</body>
</html>
```